Webdesign für Zirkeltraining für Frauen
Zielgruppe
zirkeltraining für Frauen.
Frauen jeden Alters ... 18-85 Jahre.
Aufgabenstellung
Bitte in den Farben der Bilder und der Logos bleiben. Klare Struktur. Logo wird gerade vom designer Final bearbeitet und liegt daher nur als Beispiel dem Briefing bei.

```html
<!DOCTYPE html>
<html lang="de">
<head>
<meta charset="utf-8">
<title>Velafit – Zirkeltraining für Frauen</title>
<link rel="stylesheet" href="https://fonts.googleapis.com/css2?family=Jost:wght@300;400;500;600;700&display=swap">
<style>
:root{
  --blue:#4db4df;
  --blue-dark:#3a9fcb;
  --ink:#2b2e33;
  --text:#5b6168;
  --muted:#8a9096;
  --light:#f4f6f6;
  --row-alt:#f7f8f9;
  --card-img:#dfe3e6;
  --white:#ffffff;
  --footer:#2c2f32;
  --footer-text:#e2e5e8;
}
*{margin:0;padding:0;box-sizing:border-box}
html,body{width:1200px;height:2898px;overflow:hidden}
body{position:relative;font-family:'Jost',sans-serif;color:var(--text);background:var(--white)}
.abs{position:absolute}

/* header */
.site-header{left:0;top:0;width:1200px;height:62px;background:var(--white);box-shadow:0 1px 3px rgba(0,0,0,.06);z-index:2}
.brand{left:237px;top:14px;font-size:26px;font-weight:400;letter-spacing:.18em;color:var(--ink);line-height:34px}
.brand-dot{display:inline-block;width:8px;height:8px;background:var(--blue);border-radius:50%;margin-left:6px;vertical-align:middle}
.main-nav{left:486px;top:24px;display:flex;gap:40px;font-size:10px;font-weight:600;letter-spacing:.1em;color:var(--ink)}
.main-nav .active{color:var(--blue)}

/* hero */
.hero{left:0;top:62px;width:1200px;height:438px;background:linear-gradient(100deg,#e9eef3 0%,#dbe6ee 35%,#c7d9e6 55%,#e3c9b8 70%,#d9e4ec 100%)}
.hero-title{left:229px;top:140px;font-size:50px;font-weight:700;letter-spacing:.16em;color:var(--ink);line-height:56px}
.hero-sub{left:229px;top:200px;font-size:22px;font-weight:600;letter-spacing:.12em;color:var(--ink)}
.hero-text{left:232px;top:245px;width:370px;font-size:11px;font-weight:300;line-height:17px;color:var(--text)}
.btn{display:flex;align-items:center;justify-content:center;font-weight:600;letter-spacing:.1em;text-transform:uppercase}
.btn-lg{width:123px;height:38px;font-size:10px}
.btn-fill{background:var(--blue);color:var(--white)}
.btn-line{border:1px solid var(--blue);color:var(--ink);background:rgba(255,255,255,.15)}
.btn-sm{width:81px;height:19px;font-size:6.5px}
.btn-sm.btn-line{background:var(--white)}

/* about */
.about-title{left:223px;top:594px;font-size:22px;font-weight:600;letter-spacing:.12em;color:var(--ink)}
.about-text{left:223px;top:634px;width:355px;font-size:13px;font-weight:300;line-height:22px}
.about-text p+p{margin-top:22px}
.feature-icon{width:58px;height:64px}
.feature-title{font-size:11.5px;font-weight:600;letter-spacing:.1em;color:var(--ink)}
.feature-text{width:240px;font-size:9px;font-weight:300;line-height:15.5px}

/* memberships */
.memberships{left:0;top:937px;width:1200px;height:596px;background:var(--light)}
.section-title{width:1200px;left:0;text-align:center;font-size:18px;font-weight:600;letter-spacing:.14em;color:var(--ink)}
.section-lead{left:229px;width:742px;text-align:center;font-size:11.5px;font-weight:300;line-height:16px}
.plan{top:1100px;width:226px}
.plan-head{height:93px;background:var(--blue);color:var(--white);text-align:center;padding-top:22px}
.plan-name{font-size:22px;font-weight:400;letter-spacing:.06em}
.plan-price{font-size:13.5px;font-weight:300;margin-top:2px}
.plan-row{height:37.5px;display:flex;align-items:center;justify-content:center;font-size:9px;font-weight:300;background:var(--white)}
.plan-row.off{text-decoration:line-through;color:var(--muted)}
.plan-foot{height:50px;background:var(--white);display:flex;align-items:center;justify-content:center}

/* training */
.training-photo{left:0;top:1533px;width:600px;height:511px;background:linear-gradient(120deg,#dde6ec 0%,#c9d9e4 40%,#e7d5c8 60%,#d6e2ea 100%)}
.training-title{left:600px;width:600px;text-align:center;top:1570px;font-size:18px;font-weight:600;letter-spacing:.14em;color:var(--ink)}
.training-lead{left:645px;width:510px;top:1606px;text-align:center;font-size:12px;font-weight:300;line-height:16px}
.concept{width:232px;text-align:center}
.concept .hex{width:46px;height:50px;margin:0 auto;display:block}
.concept h3{font-size:10px;font-weight:600;letter-spacing:.1em;color:var(--ink);margin-top:12px}
.concept p{font-size:8.5px;font-weight:300;line-height:13px;margin-top:8px}

/* news */
.news{left:0;top:2044px;width:1200px;height:580px;background:var(--light)}
.news-title{color:var(--blue)}
.news-card{top:2229px;width:226px;height:332px;background:var(--white);text-align:center}
.news-img{height:167px;background:var(--card-img)}
.news-card h3{font-size:14px;font-weight:600;letter-spacing:.1em;color:var(--ink);margin-top:16px}
.news-card p{font-size:8.5px;font-weight:300;line-height:15.5px;padding:0 12px;margin-top:6px}
.news-card .btn{margin:12px auto 0}

/* footer */
.site-footer{left:0;top:2624px;width:1200px;height:274px;background:var(--footer);color:var(--footer-text)}
.footer-mark{left:250px;top:2710px;width:72px;height:72px;border-radius:50%;background:var(--blue)}
.footer-brand{left:360px;top:2702px;font-size:13px;font-weight:700;letter-spacing:.06em;color:var(--white)}
.footer-text{left:360px;top:2730px;width:190px;font-size:9px;font-weight:300;line-height:15.5px;color:var(--footer-text)}
.footer-link{left:360px;top:2782px;font-size:9px;color:var(--blue);text-decoration:underline}
.footer-col h4{font-size:11px;font-weight:600;letter-spacing:.08em;color:var(--blue);text-transform:uppercase}
.footer-col ul{list-style:none;margin-top:12px}
.footer-col li{font-size:9px;font-weight:300;line-height:25px;color:var(--footer-text)}
.copyright{left:0;width:1200px;top:2868px;text-align:center;font-size:7px;letter-spacing:.05em;color:var(--footer-text)}
</style>
</head>
<body>

<header class="site-header abs">
  <div class="brand abs">VELAFIT<span class="brand-dot"></span></div>
  <nav class="main-nav abs">
    <span class="active">HOME</span><span>TRAININGSKONZEPT</span><span>MITGLIEDSCHAFT</span><span>AKTUELLES</span><span>KONTAKT</span>
  </nav>
</header>

<section class="hero abs" role="img" aria-label="Lächelnde Frau trainiert mit einer blauen Hantel im hellen Studio"></section>
<h1 class="hero-title abs">VELAFIT</h1>
<h2 class="hero-sub abs">ZIRKELTRAINING FÜR FRAUEN</h2>
<p class="hero-text abs">Lorem ipsum dolor sit amet, consectetur adipisicing elit, sed do eiusmod tempor incididunt ut labore et dolore magna aliqua. Duis aute irure dolor in reprehenderit in voluptate velit esse cillum dolore eu fugiat nulla pariatur. Ut enim ad minim veniam, quis nostrud exercitation ullamco laboris nisi ut aliquip</p>
<div class="btn btn-lg btn-fill abs" style="left:230px;top:341px">Mitgliedschaft</div>
<div class="btn btn-lg btn-line abs" style="left:365px;top:341px">Training</div>

<!-- about -->
<h2 class="about-title abs">ÜBER UNS</h2>
<div class="about-text abs">
  <p>Lorem ipsum dolor sit amet, consectetur adipisicing elit, sed do eiusmod tempor incididunt ut labore et dolore magna aliqua. Duis aute irure dolor in reprehenderit in voluptate velit esse cillum dolore eu fugiat nulla pariatur. Ut enim ad minim veniam, quis nostrud exercitation ullamco laboris nisi ut aliquip ex ea commodo!</p>
  <p>Duis aute irure dolor in reprehenderit in voluptate velit esse cillum dolore eu fugiat nulla pariatur. Excepteur sint occaecat cupidatat non proident.</p>
</div>

<svg class="feature-icon abs" style="left:657px;top:600px" viewBox="0 0 58 64">
  <polygon points="29,1 56,16.5 56,47.5 29,63 2,47.5 2,16.5" fill="var(--blue)"/>
  <g fill="none" stroke="var(--ink)" stroke-width="1.6">
    <circle cx="23" cy="27" r="6"/><circle cx="35" cy="27" r="6"/>
    <path d="M13 44c1-7 5-10 10-10s9 3 10 10M25 44c1-7 5-10 10-10s9 3 10 10"/>
  </g>
</svg>
<h3 class="feature-title abs" style="left:741px;top:597px">FRAUEN UNTER SICH</h3>
<p class="feature-text abs" style="left:741px;top:616px">Lorem Ipsum. Proin gravida nibh vel velit auctor aliquet. Aenean sollicitudin, lorem quis bibendum auctor, nisi elit consequat ipsum, nec sagittis sem nibh id elit.</p>
<div class="btn btn-sm btn-fill abs" style="left:741px;top:674px">Mehr lesen</div>

<svg class="feature-icon abs" style="left:657px;top:746px" viewBox="0 0 58 64">
  <polygon points="29,1 56,16.5 56,47.5 29,63 2,47.5 2,16.5" fill="var(--blue)"/>
  <g fill="var(--ink)"><rect x="19" y="36" width="4" height="8"/><rect x="27" y="29" width="4" height="15"/><rect x="35" y="21" width="4" height="23"/></g>
</svg>
<h3 class="feature-title abs" style="left:741px;top:744px">ALTER VON 18 BIS 85</h3>
<p class="feature-text abs" style="left:741px;top:763px">Lorem Ipsum. Proin gravida nibh vel velit auctor aliquet. Aenean sollicitudin, lorem quis bibendum auctor, nisi elit consequat ipsum, nec sagittis sem nibh id elit.</p>
<div class="btn btn-sm btn-line abs" style="left:741px;top:820px">Mehr lesen</div>

<!-- memberships -->
<section class="memberships abs"></section>
<h2 class="section-title abs" style="top:980px">MITGLIEDSCHAFTEN</h2>
<p class="section-lead abs" style="top:1017px">Lorem ipsum dolor sit amet, consectetur adipisicing elit, sed do eiusmod tempor incididunt ut labore et dolore magna aliqua. Duis aute irure dolor in reprehenderit in voluptate velit esse cillum dolore eu fugiat nulla pariatur.</p>

<div class="plan abs" style="left:229px">
  <div class="plan-head"><div class="plan-name">BEGINNER</div><div class="plan-price">€50 pro Monat</div></div>
  <div class="plan-row">1x pro Woche</div>
  <div class="plan-row" style="background:var(--row-alt)">Lorem ipsum</div>
  <div class="plan-row">Lorem ipsum</div>
  <div class="plan-row" style="background:var(--row-alt)">Lorem ipsum</div>
  <div class="plan-row off">Lorem ipsum</div>
  <div class="plan-row off" style="background:var(--row-alt)">Lorem ipsum</div>
  <div class="plan-foot"><div class="btn btn-sm btn-line">Buchen</div></div>
</div>
<div class="plan abs" style="left:487px">
  <div class="plan-head"><div class="plan-name">ERFAHREN</div><div class="plan-price">€75 pro Monat</div></div>
  <div class="plan-row">2x pro Woche</div>
  <div class="plan-row" style="background:var(--row-alt)">Lorem ipsum</div>
  <div class="plan-row">Lorem ipsum</div>
  <div class="plan-row" style="background:var(--row-alt)">Lorem ipsum</div>
  <div class="plan-row">Lorem ipsum</div>
  <div class="plan-row off" style="background:var(--row-alt)">Lorem ipsum</div>
  <div class="plan-foot"><div class="btn btn-sm btn-fill">Buchen</div></div>
</div>
<div class="plan abs" style="left:745px">
  <div class="plan-head"><div class="plan-name">EXPERTE</div><div class="plan-price">€100 pro Monat</div></div>
  <div class="plan-row">3x pro Woche</div>
  <div class="plan-row" style="background:var(--row-alt)">Lorem ipsum</div>
  <div class="plan-row">Lorem ipsum</div>
  <div class="plan-row" style="background:var(--row-alt)">Lorem ipsum</div>
  <div class="plan-row">Lorem ipsum</div>
  <div class="plan-row" style="background:var(--row-alt)">Lorem ipsum</div>
  <div class="plan-foot"><div class="btn btn-sm btn-line">Buchen</div></div>
</div>

<!-- training concept -->
<section class="training-photo abs" role="img" aria-label="Sportliche Frau trainiert mit zwei blauen Kurzhanteln"></section>
<h2 class="training-title abs">DAS TRAININGSKONZEPT</h2>
<p class="training-lead abs">Lorem ipsum dolor sit amet, consectetur adipisicing elit, sed do eiusmod tempor incididunt ut labore et dolore magna aliqua. Duis aute irure dolor in reprehenderit in voluptate velit esse cillum dolore</p>

<div class="concept abs" style="left:637px;top:1675px">
  <svg class="hex" viewBox="0 0 46 50"><polygon points="23,1 44,13 44,37 23,49 2,37 2,13" fill="var(--blue)"/><path d="M17 19l12 12M17 19h5M17 19v5M29 31h-5M29 31v-5" stroke="#fff" stroke-width="2" fill="none"/></svg>
  <h3>EIGENE GERÄTE</h3>
  <p>Lorem Ipsum. Proin gravida nibh vel velit auctor aliquet. Aenean sollicitudin, lorem quis bibendum auctor, nisi elit consequat ipsum, nec sagittis sem nibh id elit. Duis sed odio sit amet nibh vulputate cursus a sit amet mauris. Morbi accumsan ipsum velit. Nam nec tellus a odio tincidunt</p>
</div>
<div class="concept abs" style="left:927px;top:1675px">
  <svg class="hex" viewBox="0 0 46 50"><polygon points="23,1 44,13 44,37 23,49 2,37 2,13" fill="var(--blue)"/><path d="M17 19l12 12M17 19h5M17 19v5M29 31h-5M29 31v-5" stroke="#fff" stroke-width="2" fill="none"/></svg>
  <h3>TRAINING IN KLEINGRUPPEN</h3>
  <p>Lorem Ipsum. Proin gravida nibh vel velit auctor aliquet. Aenean sollicitudin, lorem quis bibendum auctor, nisi elit consequat ipsum, nec sagittis sem nibh id elit. Duis sed odio sit amet nibh vulputate cursus a sit amet mauris. Morbi accumsan ipsum velit. Nam nec tellus a odio tincidunt</p>
</div>
<div class="concept abs" style="left:637px;top:1850px">
  <svg class="hex" viewBox="0 0 46 50"><polygon points="23,1 44,13 44,37 23,49 2,37 2,13" fill="var(--blue)"/><path d="M17 19l12 12M17 19h5M17 19v5M29 31h-5M29 31v-5" stroke="#fff" stroke-width="2" fill="none"/></svg>
  <h3>ZIRKELTRAINING</h3>
  <p>Lorem Ipsum. Proin gravida nibh vel velit auctor aliquet. Aenean sollicitudin, lorem quis bibendum auctor, nisi elit consequat ipsum, nec sagittis sem nibh id elit. Duis sed odio sit amet nibh vulputate cursus a sit amet mauris. Morbi accumsan ipsum velit. Nam nec tellus a odio tincidunt</p>
</div>
<div class="concept abs" style="left:927px;top:1850px">
  <svg class="hex" viewBox="0 0 46 50"><polygon points="23,1 44,13 44,37 23,49 2,37 2,13" fill="var(--blue)"/><path d="M17 19l12 12M17 19h5M17 19v5M29 31h-5M29 31v-5" stroke="#fff" stroke-width="2" fill="none"/></svg>
  <h3>SICHERHEIT</h3>
  <p>Lorem Ipsum. Proin gravida nibh vel velit auctor aliquet. Aenean sollicitudin, lorem quis bibendum auctor, nisi elit consequat ipsum, nec sagittis sem nibh id elit. Duis sed odio sit amet nibh vulputate cursus a sit amet mauris. Morbi accumsan ipsum velit. Nam nec tellus a odio tincidunt</p>
</div>

<!-- news -->
<section class="news abs"></section>
<h2 class="section-title news-title abs" style="top:2105px">AKTUELLES</h2>
<p class="section-lead abs" style="top:2142px">Lorem ipsum dolor sit amet, consectetur adipisicing elit, sed do eiusmod tempor incididunt ut labore et dolore magna aliqua. Duis aute irure dolor in reprehenderit in voluptate velit esse cillum dolore eu fugiat nulla pariatur.</p>

<article class="news-card abs" style="left:234px">
  <div class="news-img" role="img" aria-label="Beitragsbild"></div>
  <h3>ÜBERSCHRIFT</h3>
  <p>Lorem ipsum dolor sit ametcon sectetur adipisicing elit, sed doiusmod tempor incidilabore et dolore magna aliqua. Ut enim ad mini veniam, quis nostrud exercitation ullamco laboris nisi ut aliquip ex ea</p>
  <div class="btn btn-sm btn-line">Mehr lesen</div>
</article>
<article class="news-card abs" style="left:492px">
  <div class="news-img" role="img" aria-label="Beitragsbild"></div>
  <h3>ÜBERSCHRIFT</h3>
  <p>Lorem ipsum dolor sit ametcon sectetur adipisicing elit, sed doiusmod tempor incidilabore et dolore magna aliqua. Ut enim ad mini veniam, quis nostrud exercitation ullamco laboris nisi ut aliquip ex ea</p>
  <div class="btn btn-sm btn-line">Mehr lesen</div>
</article>
<article class="news-card abs" style="left:751px">
  <div class="news-img" role="img" aria-label="Beitragsbild"></div>
  <h3>ÜBERSCHRIFT</h3>
  <p>Lorem ipsum dolor sit ametcon sectetur adipisicing elit, sed doiusmod tempor incidilabore et dolore magna aliqua. Ut enim ad mini veniam, quis nostrud exercitation ullamco laboris nisi ut aliquip ex ea</p>
  <div class="btn btn-sm btn-fill">Mehr lesen</div>
</article>

<!-- footer -->
<footer class="site-footer abs"></footer>
<div class="footer-mark abs"></div>
<div class="footer-brand abs">VELAFIT</div>
<p class="footer-text abs">Duis sed odio sit amet nibh vulputate cursus a sit amet mauris. Morbi accumsan ipsum velit. Nam nec tellus a odio cursus a sit amet mauris.</p>
<span class="footer-link abs">Mehr lesen</span>
<div class="footer-col abs" style="left:648px;top:2704px">
  <h4>Website</h4>
  <ul><li>Home</li><li>Trainingskonzept</li><li>Mitgliedschaft</li><li>Kontakt</li></ul>
</div>
<div class="footer-col abs" style="left:839px;top:2704px">
  <h4>Rechtliches</h4>
  <ul><li>Impressum</li><li>Datenschutz</li><li>AGB</li><li>Sicherheitsbestimmungen</li></ul>
</div>
<div class="copyright abs">© 2020 VELAFIT</div>

</body>
</html>
```